Banner
Zielgruppe
Wir sind Estrichleger und Beschichter. Wir erstellen u. a. Sichtestrich und Beschichtungen im Wohnbereich und für Gewerbekunden im Industriebereich (Hallen und Tiefgaragen).
Unsere Zielgruppe sind sowohl Privatverbraucher im gehobenen Segment als auch Bauträger und Gewerbekunden
Aufgabenstellung
Gute Lesbarkeit, klare Botschaft auch wenn die Banner in großer Höhe angebracht werden.
Masse:
Bauzaunbanner aus Mesh-Plane, 340x173 cm,
wird gedruckt auf
hochwertige Mehs-Plane, rundum, umsäumt und veröst, 4/0-farbig (einseitig mit Motiv bedruck), 270 g Meshgewebe-Plane - winddurchlässig und wetterfest, (B1- zertifiziert - schwer entflammbar nach DIN 4102)
Es ist wünschenswert den Claim: 'Ich steh drauf' mit auf dem Banner zu platzieren.
Wir haben gerade die Fahrzeuge neu designen lassen, der Gewinner ist hochgeladen. Gern können Sie sich an diesem orientieren.

```html
<!DOCTYPE html>
<html lang="de">
<head>
<meta charset="utf-8">
<title>Tornhaus Boden – Banner</title>
<link href="https://fonts.googleapis.com/css2?family=Roboto:wght@700&family=Roboto+Condensed:wght@300;400;700&display=swap" rel="stylesheet">
<style>
  :root {
    --black: #050505;
    --red: #a12b2b;
    --white: #ffffff;
    --photo-light: #d9d6cf;
    --photo-mid: #9c9489;
    --photo-dark: #3a3733;
  }
  html, body { margin: 0; padding: 0; overflow: hidden; background: var(--black); }
  .banner {
    position: relative;
    width: 1200px;
    height: 609px;
    background: var(--black);
    overflow: hidden;
    color: var(--white);
    font-family: "Roboto Condensed", sans-serif;
  }
  .brand-name {
    position: absolute;
    left: 50px; top: 178px;
    margin: 0;
    font-weight: 300;
    font-size: 54px;
    letter-spacing: 0.52em;
    line-height: 1;
    white-space: nowrap;
  }
  .address {
    position: absolute;
    left: 49px; top: 252px;
    margin: 0;
    font-weight: 700;
    font-size: 45px;
    line-height: 1;
    white-space: nowrap;
  }
  .trade {
    position: absolute;
    left: 719px; top: 12px;
    margin: 0;
  }
  .trade-title {
    display: block;
    font-family: "Roboto", sans-serif;
    font-weight: 700;
    font-size: 38px;
    letter-spacing: 0.2em;
    line-height: 44px;
    white-space: nowrap;
  }
  .trade-sub {
    display: block;
    font-weight: 400;
    font-size: 34.5px;
    line-height: 38px;
    white-space: nowrap;
  }
  .claim {
    position: absolute;
    left: 775px; top: 232px;
    margin: 0;
    font-family: "Roboto", sans-serif;
    font-weight: 700;
    font-size: 45px;
    letter-spacing: 0.1em;
    color: var(--red);
    white-space: nowrap;
    transform: rotate(-8deg);
    transform-origin: left bottom;
  }
  .contact {
    position: absolute;
    left: 0; top: 369px;
    width: 600px; height: 240px;
    background: var(--red);
  }
  .contact p {
    position: absolute;
    left: 49px;
    margin: 0;
    font-size: 40px;
    line-height: 1;
    white-space: nowrap;
  }
  .contact .web { top: 30px; font-weight: 700; }
  .contact .phone { top: 104px; font-weight: 400; }
  .contact .mail { top: 179px; font-weight: 400; }
  .photo {
    position: absolute;
    left: 600px; top: 369px;
    width: 600px; height: 240px;
    background: linear-gradient(135deg, var(--photo-mid) 0%, var(--photo-light) 45%, var(--photo-mid) 75%, var(--photo-dark) 100%);
  }
  .accent-bar {
    position: absolute;
    left: 866px; top: 357px;
    width: 334px; height: 19px;
    background: var(--red);
  }
</style>
</head>
<body>
<div class="banner">
  <p class="brand-name">TORNHAUS</p>
  <p class="address">Lindenweg 7 · 84021 · Almbrunn</p>

  <h1 class="trade">
    <span class="trade-title">Estrichleger</span>
    <span class="trade-title">und Beschichter</span>
    <span class="trade-sub">für Wohnhäuser und Gewerbe</span>
  </h1>

  <p class="claim">‚Ich steh drauf‘</p>

  <div class="contact">
    <p class="web">tornhaus-boden.de</p>
    <p class="phone">T: 0 12 34 / 56 78 90 0</p>
    <p class="mail">M: info@tornhaus-boden.de</p>
  </div>

  <div class="photo" role="img" aria-label="Foto: offene Galerie mit hellem Sichtestrichboden, Holzstützen, schwarzem Geländer und dunklen Sesseln"></div>
  <div class="accent-bar"></div>
</div>
</body>
</html>
```